Glow & Gloss by Mina
Text 410.582.3107 to set up and appointment
Instagram is Glow_GlossByMina
Location 4318 Fernwick Rd. Ashbury Pa, 21087 Suit 204
Slogan "Radiant Glow. Beautiful You.
Specializing in pressicion cuts, blonding, fades, perms, waxing and more

The salon is black, gun metal color mirror with led lights. Green plants and has natural wood countertops for accent colors. Modern yet elegant. I want the card simple but it needs something to really grab the clients attention. I like black, grey, gold, green, natural tones and hints of pink or gold coloring
I’m open to anything. I don’t have a logo. Suggestions are welcome

Target Market(s)

20-60 men and woman

Industry/Entity Type

Hairstylist / barber

Contact Information for Business Card

The name of the show should be bold. Maybe the letters could raised I also like foil for shine added or a mat finish

Colors

Designer to choose colors to be used in the design.

Requirements
Must have
• I also like some floral Floral designs, but not too overpowering. I like Sparkle, Watercolor design, Or a geometric line in the background
Nice to have
• I’m really here because I need creative help. I’m open for suggestions. I’ll post a picture of the salon in inspiration if I can find it.
Should not have
• Checkered background

```html
<!DOCTYPE html>
<html lang="en">
<head>
<meta charset="utf-8">
<title>Glow &amp; Gloss by Mina – Business Card</title>
<link href="https://fonts.googleapis.com/css2?family=Playfair+Display:wght@700&family=Roboto+Condensed:wght@400&display=swap" rel="stylesheet">
<style>
  :root {
    --backdrop: #6b6f71;
    --card: #222328;
    --gold: #d2a63c;
    --gold-soft: #c29a3a;
    --floral-dark: #2b2a27;
    --floral-gold: #6e5a2c;
  }
  * { box-sizing: border-box; margin: 0; padding: 0; }
  html, body { width: 1200px; height: 780px; overflow: hidden; }
  body {
    background: var(--backdrop);
    display: flex;
    flex-direction: column;
    align-items: center;
    justify-content: center;
    gap: 40px;
    font-family: "Roboto Condensed", "Arial Narrow", sans-serif;
  }
  .card {
    position: relative;
    width: 600px;
    height: 330px;
    background: var(--card);
    border-radius: 22px;
    overflow: hidden;
    box-shadow: 0 10px 24px rgba(0,0,0,0.35);
  }
  .brand-name {
    font-family: "Playfair Display", Georgia, serif;
    font-weight: 700;
    color: var(--gold);
    line-height: 1.05;
    text-align: center;
    white-space: nowrap;
  }
  .brand-by { display: block; }

  /* Front */
  .card--front .brand-name {
    position: absolute;
    left: 50%;
    top: 44%;
    transform: translate(-50%, -50%);
    font-size: 50px;
  }
  .card--front .brand-by { font-size: 30px; margin-top: 14px; }
  .floral {
    position: absolute;
    background: radial-gradient(ellipse at center, var(--floral-gold) 0%, var(--floral-dark) 55%, transparent 75%);
    opacity: 0.8;
  }
  .floral--left { left: -60px; top: 40px; width: 200px; height: 290px; }
  .floral--right-top { right: -60px; top: -40px; width: 170px; height: 190px; }
  .floral--right-bottom { right: -40px; bottom: -60px; width: 220px; height: 190px; }

  /* Back */
  .card--back .brand-name {
    position: absolute;
    left: 30px;
    top: 120px;
    width: 240px;
    font-size: 32px;
  }
  .card--back .brand-by { font-size: 20px; margin-top: 8px; }
  .divider {
    position: absolute;
    left: 286px;
    top: 50px;
    width: 3px;
    height: 150px;
    background: var(--gold);
    border-radius: 2px;
  }
  .contact-list {
    position: absolute;
    left: 312px;
    top: 58px;
    list-style: none;
    color: var(--gold);
    font-size: 15px;
    line-height: 1.25;
  }
  .contact-list li {
    display: flex;
    align-items: flex-start;
    gap: 10px;
    margin-bottom: 12px;
  }
  .contact-icon { width: 16px; height: 16px; flex: none; margin-top: 1px; }
  .tagline {
    position: absolute;
    left: 0;
    right: 0;
    top: 228px;
    text-align: center;
    color: var(--gold);
  }
  .tagline__slogan { font-size: 24px; line-height: 1.2; }
  .tagline__services { font-size: 15px; color: var(--gold-soft); margin-top: 4px; line-height: 1.3; }
</style>
</head>
<body>

  <section class="card card--front">
    <div class="floral floral--left" role="img" aria-label="Gold line-art flowers and leaves in the left corner"></div>
    <div class="floral floral--right-top" role="img" aria-label="Gold line-art leaves in the top right corner"></div>
    <div class="floral floral--right-bottom" role="img" aria-label="Gold line-art flowers and leaves in the bottom right corner"></div>
    <h1 class="brand-name">Glow &amp; Gloss <span class="brand-by">by Mina</span></h1>
  </section>

  <section class="card card--back">
    <h2 class="brand-name">Glow &amp; Gloss <span class="brand-by">by Mina</span></h2>
    <div class="divider"></div>
    <ul class="contact-list">
      <li>
        <svg class="contact-icon" viewBox="0 0 16 16" fill="none" stroke="#d2a63c" stroke-width="1.4">
          <path d="M2 3h12v8H7l-3 3v-3H2z"/>
          <line x1="5" y1="6" x2="11" y2="6"/><line x1="5" y1="8.5" x2="9" y2="8.5"/>
        </svg>
        <span>410.582.3107</span>
      </li>
      <li>
        <svg class="contact-icon" viewBox="0 0 16 16" fill="none" stroke="#d2a63c" stroke-width="1.4">
          <circle cx="8" cy="8" r="6"/>
        </svg>
        <span>Glow_GlossByMina</span>
      </li>
      <li>
        <svg class="contact-icon" viewBox="0 0 16 16" fill="none" stroke="#d2a63c" stroke-width="1.4">
          <path d="M8 14s-4.5-4.6-4.5-8A4.5 4.5 0 0 1 12.5 6c0 3.4-4.5 8-4.5 8z"/>
          <circle cx="8" cy="6" r="1.6"/>
        </svg>
        <span>4318 Fernwick Rd. Ashbury<br>Pa,21087 Suit 204</span>
      </li>
    </ul>
    <div class="tagline">
      <p class="tagline__slogan">“Radiant Glow. Beautiful You”</p>
      <p class="tagline__services">Specializing in pressicion cuts, blonding,<br>fades, perms, waxing and more</p>
    </div>
  </section>

</body>
</html>
```